5 Planner Covers for Teacher Planners

Hello,
I currently run a Speech-Language Pathologist website and have created a planner for my fellow Speech Therapist. I would like someone to create 5 different planner covers so my followers will have different options to choose from.
Here is my planner from last year to give you an idea of what the planner will look like http://www.talkwellnook.example/free-slp-planner/
My followers are mostly women aged 25-50. However, I don't want the covers to be overly girly or excessive with flowers. Simple is better.
I'd also like there to be an editable text box to allow the Speech Therapist to type their name on their cover if they wish.
Planner Cover can say any of the following: SLP Planner, Planner, Speech Therapy Planner, Speech-Language Pathologist (maybe this title could be editable as well??).
To give you an idea I have uploaded a screenshot of last year's planners cover that I made myself.
What I am looking for:
-Size 8.5" by 11"
-5 different planner covers
-1 gender-neutral cover
-simple design
-limited flowers (or overly girly
-text box to add a personal name
-Possible titles: SLP Planner, Planner, Speech Therapy Planner, Speech-Language Pathologist (maybe this title could be editable as well??)
Target Market(s)
Women aged 25-50
Colors
Designer to choose colors to be used in the design.
Requirements
Must have
- What I am looking for:
-Size 8.5" by 11"
-1 gender-neutral cover
-simple design
Nice to have
- I've uploaded some that I like from Craftly to give you an idea.
Here is my craftly store https://www.craftly.example/shop/QuietMeadowHome to give you an idea of things I like.
I like Marla Hensley and her simple elegant rustic style.

```html
<!DOCTYPE html>
<html lang="en">
<head>
<meta charset="UTF-8">
<title>SLP Planner Cover</title>
<link href="https://fonts.googleapis.com/css2?family=Josefin+Sans:wght@100;200&family=Dancing+Script:wght@600;700&family=Montserrat:wght@300&display=swap" rel="stylesheet">
<style>
  :root {
    --paper: #f6f0eb;
    --paper-shade: #efe7e1;
    --rose-deep: #9b5855;
    --rose-soft: #c8a79f;
    --wash-pink: #f0bdb8;
    --wash-light: #f6d6d0;
    --wash-sage: #e7d9cc;
  }
  * { margin: 0; padding: 0; box-sizing: border-box; }
  html, body {
    width: 927px;
    height: 1200px;
    overflow: hidden;
    background: var(--paper);
  }
  .cover {
    position: relative;
    width: 927px;
    height: 1200px;
    overflow: hidden;
    background: radial-gradient(ellipse at 30% 40%, var(--paper) 0%, var(--paper-shade) 100%);
  }
  .decor { position: absolute; display: block; }
  .wash-top { left: 385px; top: 0; width: 542px; height: 155px; }
  .wash-bottom { left: 150px; top: 1045px; width: 650px; height: 155px; }
  .iris-title { left: 477px; top: 255px; width: 165px; height: 215px; }
  .iris-corner { left: 0; top: 810px; width: 300px; height: 390px; }

  .title {
    position: absolute;
    left: 270px;
    top: 341px;
    font-weight: normal;
  }
  .title-main {
    display: block;
    font-family: "Josefin Sans", sans-serif;
    font-weight: 100;
    font-size: 150px;
    line-height: 1;
    letter-spacing: 2px;
    color: var(--rose-deep);
  }
  .title-sub {
    position: absolute;
    left: 147px;
    top: 109px;
    font-family: "Dancing Script", cursive;
    font-weight: 700;
    font-size: 84px;
    line-height: 1;
    color: var(--rose-soft);
    white-space: nowrap;
  }
  .owner {
    position: absolute;
    left: 512px;
    top: 912px;
  }
  .owner-label {
    font-family: "Montserrat", sans-serif;
    font-weight: 300;
    font-size: 21px;
    color: var(--rose-deep);
    white-space: nowrap;
  }
  .owner-name {
    margin-top: 4px;
    margin-left: 68px;
    font-family: "Dancing Script", cursive;
    font-weight: 700;
    font-size: 56px;
    line-height: 1.1;
    color: var(--rose-soft);
    white-space: nowrap;
  }
</style>
</head>
<body>
<main class="cover">
  <svg class="decor wash-top" viewBox="0 0 542 155" role="img" aria-label="Soft pink watercolour wash in the top corner">
    <defs>
      <linearGradient id="washTopFill" x1="0" y1="0" x2="1" y2="0">
        <stop offset="0" stop-color="var(--wash-light)" stop-opacity="0.5"/>
        <stop offset="0.35" stop-color="var(--wash-pink)" stop-opacity="0.85"/>
        <stop offset="1" stop-color="var(--wash-pink)" stop-opacity="0.9"/>
      </linearGradient>
    </defs>
    <path d="M30 0 H542 V150 C470 150 380 140 300 128 C240 120 200 100 180 90 C120 70 60 60 20 55 C0 35 10 10 30 0 Z" fill="url(#washTopFill)"/>
  </svg>

  <svg class="decor wash-bottom" viewBox="0 0 650 155" role="img" aria-label="Soft pink watercolour wash along the bottom edge">
    <defs>
      <linearGradient id="washBottomFill" x1="0" y1="0" x2="1" y2="1">
        <stop offset="0" stop-color="var(--wash-pink)" stop-opacity="0.8"/>
        <stop offset="0.6" stop-color="var(--wash-light)" stop-opacity="0.75"/>
        <stop offset="1" stop-color="var(--wash-sage)" stop-opacity="0.5"/>
      </linearGradient>
    </defs>
    <path d="M40 30 C150 10 320 15 400 40 C480 55 600 70 640 95 C650 130 620 155 600 155 H20 C0 120 10 60 40 30 Z" fill="url(#washBottomFill)"/>
  </svg>

  <svg class="decor iris-title" viewBox="0 0 165 215" role="img" aria-label="Fine line illustration of a single iris flower on a tall stem">
    <defs>
      <radialGradient id="irisSmallFill" cx="0.5" cy="0.3" r="0.6">
        <stop offset="0" stop-color="var(--wash-light)" stop-opacity="0.6"/>
        <stop offset="1" stop-color="var(--paper)" stop-opacity="0"/>
      </radialGradient>
    </defs>
    <rect width="165" height="215" fill="url(#irisSmallFill)"/>
  </svg>

  <svg class="decor iris-corner" viewBox="0 0 300 390" role="img" aria-label="Fine line illustration of iris flowers and buds rising from the lower left corner">
    <defs>
      <radialGradient id="irisCornerFill" cx="0.4" cy="0.4" r="0.6">
        <stop offset="0" stop-color="var(--wash-light)" stop-opacity="0.55"/>
        <stop offset="1" stop-color="var(--paper)" stop-opacity="0"/>
      </radialGradient>
    </defs>
    <rect width="300" height="390" fill="url(#irisCornerFill)"/>
  </svg>

  <h1 class="title">
    <span class="title-main">SLP</span>
    <span class="title-sub">planner</span>
  </h1>

  <section class="owner">
    <p class="owner-label">This planner belongs to</p>
    <p class="owner-name">Delia Warren</p>
  </section>
</main>
</body>
</html>
```